Home page graphic design only (NOT WEBSITE DESIGN)

I require a home page to be designed for my new website.
I DO NOT REQUIRE to build a website. We are a rug company specialising in alpaca wool. It is targeted at the high end of the market and hence the graphics of our page requires to reflect this. Our current page is as per attachment and I think it is too basic.
Updates

Target Market(s)

Extremly high net worth individuals where luxury is a requirement

Requirements
Must have
• show of style, luxury, uniqueness. Prefer having bright images.
Nice to have
• a highly sofisticated roomscape where the focus in the rug. See attachment as an example
Should not have
• Not sure

```html
<!DOCTYPE html>
<html lang="en">
<head>
<meta charset="utf-8">
<title>Lune Douce – Home</title>
<link rel="stylesheet" href="https://fonts.googleapis.com/css2?family=Libre+Baskerville:wght@400;700&family=Open+Sans:wght@400;600&family=Questrial&display=swap">
<style>
  :root{
    --gold:#f5b82a;
    --ink:#111111;
    --grey-text:#555555;
    --soft-text:#666666;
    --nav-band:rgba(228,228,228,0.85);
    --white:#ffffff;
    --wood-light:#d9a57a;
    --wood-mid:#c68a5c;
    --rug:#f4f1ee;
    --icon:#333333;
  }
  *{margin:0;padding:0;box-sizing:border-box;}
  html,body{width:1200px;height:675px;overflow:hidden;background:var(--white);}
  .page{position:relative;width:1200px;height:675px;overflow:hidden;}
  .hero-scene{
    position:absolute;inset:0;
    background:
      radial-gradient(ellipse 52% 46% at 50% 88%, var(--rug) 0%, rgba(244,241,238,0.95) 55%, rgba(244,241,238,0) 100%),
      linear-gradient(180deg, #ffffff 0%, #fbfaf9 30%, rgba(250,246,242,0.9) 45%, rgba(230,190,155,0.75) 62%, var(--wood-light) 80%, var(--wood-mid) 100%);
  }
  .hero-scene::after{
    content:"";position:absolute;inset:0;
    background:linear-gradient(90deg, rgba(255,255,255,0) 0%, rgba(255,255,255,0.55) 35%, rgba(255,255,255,0.55) 65%, rgba(255,255,255,0) 100%);
  }
  .brand{
    position:absolute;top:26px;left:0;width:100%;text-align:center;
    font-family:"Libre Baskerville",serif;font-weight:400;font-size:36px;color:var(--gold);
  }
  .nav-band{position:absolute;top:95px;left:0;width:100%;height:45px;background:var(--nav-band);}
  .nav{position:absolute;left:177px;top:0;height:45px;display:flex;list-style:none;
    font-family:"Open Sans",sans-serif;font-size:11.5px;color:var(--ink);}
  .nav li{height:45px;line-height:45px;padding:0 16.5px;}
  .nav li.is-active{background:var(--gold);}
  .nav .caret{font-size:7px;margin-left:4px;color:#777;}
  .contact-mail{position:absolute;right:179px;top:0;height:45px;display:flex;align-items:center;gap:9px;
    font-family:"Open Sans",sans-serif;font-size:11.5px;color:var(--ink);}
  .headline{position:absolute;left:0;width:100%;text-align:center;font-family:"Libre Baskerville",serif;}
  .headline--lead{top:258px;font-size:47px;color:var(--grey-text);font-weight:400;}
  .headline--main{top:325px;font-size:43px;color:var(--ink);font-weight:700;letter-spacing:0.5px;}
  .headline--sub{top:383px;font-size:28px;color:var(--soft-text);font-weight:400;}
  .facts{position:absolute;left:0;width:100%;text-align:center;font-family:"Questrial",sans-serif;color:#222;}
  .facts--est{top:462px;font-size:8px;}
  .facts--regions{top:479px;font-size:10.5px;}
  .facts--company{top:500px;font-size:8px;}
  .facts--abn{top:519px;font-size:8px;}
  .footer-note{position:absolute;left:178px;top:649px;font-family:"Questrial",sans-serif;font-size:8px;color:var(--ink);}
  .social{position:absolute;left:879px;top:642px;display:flex;gap:12px;}
  .social span{display:block;width:19px;height:19px;border-radius:50%;background:var(--icon);}
</style>
</head>
<body>
<div class="page">
  <div class="hero-scene" role="img" aria-label="Bright living room with a white shaggy alpaca rug on a warm timber floor"></div>

  <div class="brand">Lune Douce</div>

  <div class="nav-band">
    <ul class="nav">
      <li class="is-active">Home</li>
      <li>Collections<span class="caret">▼</span></li>
      <li>Our Story</li>
      <li>About us</li>
      <li>FAQ</li>
      <li>Publications</li>
      <li>News &amp; Events</li>
      <li>Contac us</li>
    </ul>
    <div class="contact-mail">
      <svg width="16" height="11" viewBox="0 0 16 11" aria-hidden="true">
        <rect x="0" y="0" width="16" height="11" fill="#111"/>
        <path d="M0 0 L8 6 L16 0" fill="none" stroke="#e4e4e4" stroke-width="1.2"/>
      </svg>
      <span>info@lunedouce.com</span>
    </div>
  </div>

  <h1 class="headline headline--lead">Exquisite Luxury</h1>
  <h2 class="headline headline--main">CARPETING AND AREA RUGS</h2>
  <p class="headline headline--sub">made from pure peruvian alpaca</p>

  <p class="facts facts--est">Established in 1988</p>
  <p class="facts facts--regions">Australia ~ USA ~ Europe ~ UK ~ Asia ~ UAE</p>
  <p class="facts facts--company">Lune Douce Pty Ltd</p>
  <p class="facts facts--abn">ABN 12-345-678-901</p>

  <p class="footer-note">Copyright @2020 Lune Douce - Australia - Head Office - Suite 4 / Unit 12 - 88 Willow Bend Road; Willow Bend VIC 3000</p>

  <div class="social" aria-label="Social links">
    <span></span><span></span><span></span><span></span><span></span>
  </div>
</div>
</body>
</html>
```